Marrow Airways Group Envelope, Letterhead, Business Card Design

I need designs for a new company letterhead, business cards, and envelopes. These designs will need to be presented using 5 different company logos for the different divisions that are managed under the Marrow Airways Group umbrella (company names listed below). The member of QTFL logo should also be included.
- Marrow Airways Group
- Marrow Jet Management
- Marrow Jet Charter
- Marrow Pilot Services
- Marrow Aircraft Sales
- Marrow Flight Training

Logos for the various companies are attached as well as a screen shot of the main page of our website.

```html
<!DOCTYPE html>
<html lang="en">
<head>
<meta charset="utf-8">
<title>Marrow Airways Group Stationery</title>
<link href="https://fonts.googleapis.com/css2?family=Michroma&display=swap" rel="stylesheet">
<style>
  :root {
    --brand-blue: #0061ae;
    --ink: #111111;
    --paper: #ffffff;
    --backdrop: #ffffff;
    --shadow: rgba(0, 0, 0, 0.28);
  }
  html, body {
    margin: 0;
    padding: 0;
    width: 1200px;
    height: 1200px;
    overflow: hidden;
    background: var(--backdrop);
    font-family: "Michroma", sans-serif;
    color: var(--ink);
  }
  .canvas {
    position: relative;
    width: 1200px;
    height: 1200px;
  }
  .sheet {
    position: absolute;
    background: var(--paper);
    box-shadow: 0 8px 28px var(--shadow);
    overflow: hidden;
  }
  .brand-name {
    position: absolute;
    color: var(--brand-blue);
    font-weight: 400;
    text-transform: uppercase;
    line-height: 1;
    white-space: nowrap;
  }
  .brand-name .line-main { display: block; }
  .brand-name .line-sub { display: block; }

  .contact {
    position: absolute;
    text-transform: uppercase;
    white-space: nowrap;
  }
  .contact-name {
    font-size: 11px;
    padding-bottom: 3px;
    border-bottom: 1.5px solid var(--brand-blue);
    display: inline-block;
    letter-spacing: 0.02em;
  }
  .contact-row {
    display: flex;
    align-items: center;
    gap: 2px;
    font-size: 7.5px;
    margin-top: 4px;
    letter-spacing: 0.04em;
  }
  .contact-row svg { width: 11px; height: 11px; flex: none; }

  /* Letterhead */
  .letterhead { left: 93px; top: 260px; width: 533px; height: 698px; }
  .letterhead .brand-name { left: 30px; top: 44px; }
  .letterhead .line-main { font-size: 26px; letter-spacing: 0.04em; }
  .letterhead .line-sub { font-size: 12.5px; margin-top: 6px; letter-spacing: 0.05em; }
  .letterhead .contact { left: 399px; top: 40px; }
  .letterhead-rule {
    position: absolute; left: 0; top: 117px; width: 100%; height: 2px;
    background: var(--brand-blue);
  }

  /* Business card front */
  .card-front { left: 741px; top: 214px; width: 286px; height: 166px; }
  .card-front .brand-name { left: 0; right: 0; top: 68px; text-align: center; }
  .card-front .line-main { font-size: 24px; letter-spacing: 0.04em; }
  .card-front .line-sub { font-size: 11.5px; margin-top: 6px; letter-spacing: 0.05em; }

  /* Business card back */
  .card-back { left: 742px; top: 398px; width: 286px; height: 167px; }
  .card-back .brand-name { right: 22px; top: 22px; text-align: left; }
  .card-back .line-main { font-size: 12px; letter-spacing: 0.04em; }
  .card-back .line-sub { font-size: 6px; margin-top: 3px; letter-spacing: 0.05em; }
  .card-back .contact { left: 14px; top: 96px; }
  .card-band { position: absolute; left: 0; bottom: 0; width: 100%; height: 16px; }

  /* Envelope */
  .envelope-back { left: 739px; top: 620px; width: 395px; height: 159px; background: var(--brand-blue); }
  .envelope-front { left: 739px; top: 796px; width: 395px; height: 159px; }
  .envelope-flap { position: absolute; left: 0; top: 0; width: 395px; height: 50px; }
  .envelope-front .brand-name { right: 22px; top: 108px; }
  .envelope-front .line-main { font-size: 15px; letter-spacing: 0.04em; }
  .envelope-front .line-sub { font-size: 7.5px; margin-top: 4px; letter-spacing: 0.05em; }
</style>
</head>
<body>
<div class="canvas">

  <!-- Letterhead -->
  <section class="sheet letterhead">
    <div class="brand-name">
      <span class="line-main">Marrow</span>
      <span class="line-sub">Airways Group</span>
    </div>
    <div class="contact">
      <div class="contact-name">Your Name</div>
      <div class="contact-row">
        <svg viewBox="0 0 12 12"><circle cx="6" cy="6" r="5.2" fill="none" stroke="#111" stroke-width="0.9"/><rect x="3.3" y="4.2" width="5.4" height="3.6" fill="#111"/><path d="M3.3 4.3 L6 6.3 L8.7 4.3" fill="none" stroke="#fff" stroke-width="0.5"/></svg>
        <span>Your Email</span>
      </div>
      <div class="contact-row">
        <svg viewBox="0 0 12 12"><circle cx="6" cy="6" r="5.2" fill="none" stroke="#111" stroke-width="0.9"/><path d="M4 3.4 L5 3.2 L5.5 4.8 L4.9 5.3 Q5.5 6.6 6.7 7.1 L7.2 6.5 L8.8 7 L8.6 8 Q7.8 8.8 6.5 8.2 Q4.3 7.1 3.6 5 Q3.3 4 4 3.4 Z" fill="#111"/></svg>
        <span>Yourphone</span>
      </div>
    </div>
    <div class="letterhead-rule"></div>
  </section>

  <!-- Business card front -->
  <section class="sheet card-front">
    <div class="brand-name">
      <span class="line-main">Marrow</span>
      <span class="line-sub">Airways Group</span>
    </div>
  </section>

  <!-- Business card back -->
  <section class="sheet card-back">
    <div class="brand-name">
      <span class="line-main">Marrow</span>
      <span class="line-sub">Airways Group</span>
    </div>
    <div class="contact">
      <div class="contact-name">Your Name</div>
      <div class="contact-row">
        <svg viewBox="0 0 12 12"><circle cx="6" cy="6" r="5.2" fill="none" stroke="#111" stroke-width="0.9"/><rect x="3.3" y="4.2" width="5.4" height="3.6" fill="#111"/><path d="M3.3 4.3 L6 6.3 L8.7 4.3" fill="none" stroke="#fff" stroke-width="0.5"/></svg>
        <span>Your Email</span>
      </div>
      <div class="contact-row">
        <svg viewBox="0 0 12 12"><circle cx="6" cy="6" r="5.2" fill="none" stroke="#111" stroke-width="0.9"/><path d="M4 3.4 L5 3.2 L5.5 4.8 L4.9 5.3 Q5.5 6.6 6.7 7.1 L7.2 6.5 L8.8 7 L8.6 8 Q7.8 8.8 6.5 8.2 Q4.3 7.1 3.6 5 Q3.3 4 4 3.4 Z" fill="#111"/></svg>
        <span>Yourphone</span>
      </div>
    </div>
    <svg class="card-band" viewBox="0 0 286 16" preserveAspectRatio="none">
      <polygon points="0,0 153,0 140,16 0,16" fill="var(--brand-blue)"/>
      <polygon points="158,0 286,0 286,16 145,16" fill="var(--brand-blue)"/>
    </svg>
  </section>

  <!-- Envelope back -->
  <section class="sheet envelope-back"></section>

  <!-- Envelope front -->
  <section class="sheet envelope-front">
    <svg class="envelope-flap" viewBox="0 0 395 50">
      <path d="M0 0 H395 L384 36 Q380 48 364 48 H31 Q15 48 11 36 Z" fill="var(--brand-blue)"/>
    </svg>
    <div class="brand-name">
      <span class="line-main">Marrow</span>
      <span class="line-sub">Airways Group</span>
    </div>
  </section>

</div>
</body>
</html>
```